Anzeige zur Kundenakquise
Zielgruppe
Wir sind der größte unabhängige Versicherungsmakler Deutschlands.
https://www.vendler-tarifkreis.de/
Aufgabenstellung
Die Anzeige dient zur Kundenakquise. Der Flyer soll in erster Linie auf Trivolo veröffentlicht werden.
Sie soll Kunden anregen eine Nachricht an uns zu schicken und einen Termin bis zum 30.11.2018 zu vereinbaren um ihre KFZ-Versicherungen vergleichen zu lassen.
Der alte Flyer wird mit hochgeladen. Bitte den Text nicht 1 zu 1 übernehmen.
Farbe und Stil sollten übernommen werden.
Die Maße für Trivolo:
Empfohlene Bildgröße:
1.200 x 628 Pixel
Bildseitenverhältnis: 1,91:1
Auf Grund der Zusendung von mehrerern Flyer der Designer bitte ich die Anzahl auf 3 zu einigen, d.h. bitte senden Sie für eine Trivolo Slidekampane 3 Flyer als ein Projekt zu. Vielen Dank für Ihre Mühe.

```html
<!DOCTYPE html>
<html lang="de">
<head>
<meta charset="utf-8">
<title>KFZ-Versicherung wechseln – Vendler Tarifkreis</title>
<link rel="stylesheet" href="https://fonts.googleapis.com/css2?family=Roboto:wght@400;500;700&display=swap">
<style>
  :root {
    --green: #8cc21f;
    --green-dark: #7fb01a;
    --grey-text: #58595b;
    --grey-panel: rgba(90, 90, 90, 0.92);
    --white: #ffffff;
  }
  * { margin: 0; padding: 0; box-sizing: border-box; }
  html, body { width: 1200px; height: 628px; overflow: hidden; background: var(--white); }
  body { font-family: "Roboto", Arial, sans-serif; }
  .ad {
    position: relative;
    width: 1200px;
    height: 628px;
    overflow: hidden;
    background: var(--white);
  }
  .hero-photo {
    position: absolute;
    left: 0; top: 0;
    width: 1200px; height: 494px;
    background:
      radial-gradient(ellipse 420px 300px at 1050px 120px, rgba(235, 240, 215, 0.9), transparent 70%),
      radial-gradient(ellipse 300px 260px at 1100px 420px, rgba(150, 160, 90, 0.7), transparent 70%),
      linear-gradient(100deg, #2e6f86 0%, #4f93a8 30%, #7e3b34 55%, #b04a3c 62%, #a9ad7a 75%, #d9dcc0 100%);
  }
  .accent-line {
    position: absolute;
    left: 0; top: 492px;
    width: 1200px; height: 7px;
    background: var(--green);
  }
  .headline-box {
    position: absolute;
    left: -4px; top: 253px;
    width: 667px; height: 150px;
    background: var(--green);
    border: 3px solid var(--white);
    color: var(--white);
    font-weight: 700;
    font-size: 45px;
    line-height: 58px;
    letter-spacing: 0.5px;
    padding: 17px 0 0 72px;
    text-transform: uppercase;
  }
  .deadline-box {
    position: absolute;
    left: 740px; top: 70px;
    width: 433px; height: 128px;
    border: 3px solid var(--white);
    background: var(--grey-panel);
  }
  .deadline-date {
    height: 86px;
    color: var(--white);
    font-weight: 700;
    font-size: 52px;
    line-height: 86px;
    text-align: center;
    letter-spacing: 0.5px;
  }
  .deadline-date .highlight { color: var(--green); }
  .deadline-action {
    height: 36px;
    margin: 0 3px;
    background: var(--green);
    color: var(--white);
    font-weight: 700;
    font-size: 24px;
    line-height: 36px;
    text-align: center;
  }
  .savings-badge {
    position: absolute;
    left: 889px; top: 241px;
    width: 222px; height: 222px;
    border-radius: 50%;
    background: var(--green);
    border: 3px solid var(--white);
    color: var(--white);
    font-weight: 700;
    text-align: center;
  }
  .savings-badge .small { display: block; font-size: 23px; line-height: 26px; }
  .savings-badge .small.top { margin-top: 46px; }
  .savings-badge .big { display: block; font-size: 80px; line-height: 84px; letter-spacing: -1px; }
  .call-to-action {
    position: absolute;
    left: 0; top: 534px;
    width: 1200px;
    text-align: center;
    padding-right: 60px;
    color: var(--grey-text);
    font-weight: 500;
    font-size: 44px;
    line-height: 60px;
    letter-spacing: 0.5px;
  }
  .call-to-action .highlight { color: var(--green); font-weight: 700; }
  .brand {
    position: absolute;
    left: 1058px; top: 534px;
    display: flex;
    align-items: flex-start;
    gap: 6px;
  }
  .brand-square {
    width: 22px; height: 22px;
    background: var(--green);
    margin-top: 4px;
  }
  .brand-name {
    color: var(--grey-text);
    font-weight: 700;
    font-size: 15px;
    line-height: 17px;
    text-transform: uppercase;
  }
</style>
</head>
<body>
<main class="ad">
  <div class="hero-photo" role="img" aria-label="Foto: Mann mit Brille am Steuer eines roten Autos, Blick durch die Seitenscheibe, unscharfer grüner Hintergrund"></div>
  <div class="accent-line"></div>

  <div class="headline-box">
    Schluss mit teuren<br>KFZ-Versicherungen
  </div>

  <div class="deadline-box">
    <div class="deadline-date">BIS ZUM <span class="highlight">30.11</span></div>
    <div class="deadline-action">KFZ-VERSICHERUNG WECHSELN</div>
  </div>

  <div class="savings-badge">
    <span class="small top">BIS ZU</span>
    <span class="big">40%</span>
    <span class="small">SPAREN!</span>
  </div>

  <p class="call-to-action">VEREINBAREN SIE <span class="highlight">GLEICH</span> EINEN TERMIN!</p>

  <div class="brand">
    <span class="brand-square"></span>
    <span class="brand-name">Vendler<br>Tarifkreis</span>
  </div>
</main>
</body>
</html>
```